Business Card Design Project

I need a business card design for our new logo, please check the logo at the following link:
https://www.filecrate.net/s/q7rtx2pw9kd41m/FernLoop.png
The address on the business card:
Av. Gervásio Tavares 418 sala 207
Barra da Tijuca, Rio de Janeiro, RJ
CEP: 22714-380
Brasil
Phone: +55 21 86347215
e-mail: osvaldo@fernloop.com.br
Updates
Thank you all for sending your designs, we will not provide feedback because there are too many designs, on December 3 we will pick the best design according to our point of view. Please keep posting.
Osvaldo
Industry/Entity Type
Business
Look and feel
Each slider illustrates characteristics of the customer's brand and the style your logo design should communicate.

```html
<!DOCTYPE html>
<html lang="pt-BR">
<head>
<meta charset="UTF-8">
<title>FernLoop – Business Card</title>
<link href="https://fonts.googleapis.com/css2?family=Montserrat:wght@400;500;800&display=swap" rel="stylesheet">
<style>
  :root {
    --bg: #e9e4df;
    --card-white: #ffffff;
    --card-black: #141414;
    --ink: #1a1a1a;
    --accent: #f4bf00;
    --paper-light: #ffffff;
  }
  * { box-sizing: border-box; margin: 0; padding: 0; }
  html, body {
    width: 1200px; height: 900px; overflow: hidden;
    background: var(--bg);
    font-family: "Montserrat", Arial, sans-serif;
  }
  .canvas {
    position: relative; width: 1200px; height: 900px;
  }
  .card {
    position: absolute; left: 290px;
    width: 620px; height: 354px;
    box-shadow: 0 6px 18px rgba(0,0,0,0.18);
  }
  .card--front { top: 68px; background: var(--card-white); }
  .card--back  { top: 470px; background: var(--card-black); }

  .brand {
    position: absolute; display: flex; align-items: center; gap: 12px;
    font-weight: 800; letter-spacing: -0.5px;
  }
  .brand__square { background: var(--accent); }
  .card--front .brand { left: 48px; top: 150px; color: var(--ink); font-size: 44px; }
  .card--front .brand__square { width: 30px; height: 30px; }
  .card--back .brand {
    left: 50%; top: 50%; transform: translate(-50%, -50%);
    color: var(--paper-light); font-size: 64px;
  }
  .card--back .brand__square { width: 42px; height: 42px; }

  .contact {
    position: absolute; right: 40px; top: 46px;
    text-align: right; color: var(--ink);
    font-size: 14px; line-height: 1.32; font-weight: 400;
  }
  .contact__name {
    font-weight: 800; font-size: 24px; letter-spacing: -0.5px; line-height: 1;
  }
  .contact__first { color: var(--ink); }
  .contact__last { color: var(--accent); }
  .contact__role {
    font-weight: 500; font-size: 13px; letter-spacing: 0.6px; margin-bottom: 14px;
  }
  .contact__block + .contact__block { margin-top: 14px; }
</style>
</head>
<body>
<main class="canvas">
  <section class="card card--front">
    <div class="brand">
      <span class="brand__square"></span>
      <span class="brand__name">FernLoop</span>
    </div>
    <div class="contact">
      <p class="contact__name"><span class="contact__first">Osvaldo</span><span class="contact__last">Torrente</span></p>
      <p class="contact__role">MANAGING DIRECTOR</p>
      <address class="contact__block" style="font-style:normal">
        Av. Gervásio Tavares 418 sala 207<br>
        Barra da Tijuca, Rio de Janeiro, RJ<br>
        CEP: 22714-380<br>
        Brasil
      </address>
      <p class="contact__block">
        p: +55 21 86347215<br>
        osvaldo@fernloop.com.br<br>
        www.fernloop.com.br
      </p>
    </div>
  </section>

  <section class="card card--back">
    <div class="brand">
      <span class="brand__square"></span>
      <span class="brand__name">FernLoop</span>
    </div>
  </section>
</main>
</body>
</html>
```